Need standup pouch design (Sri Lankan theme) for True Ceylon Cinnamon with MCT Oil:
- Organic
- 100% Vegetarian
- GMO Free
- Gluten Free
- 3rd Party Tested

```html
<!DOCTYPE html>
<html lang="en">
<head>
<meta charset="utf-8">
<title>Ceylon Cinnamon – Stand-up Pouch Front</title>
<link rel="stylesheet" href="https://fonts.googleapis.com/css2?family=Archivo+Black&family=Poppins:wght@700;800;900&family=Pacifico&display=swap">
<style>
  :root {
    --stage: #efe6dc;
    --orange: #ec7a1c;
    --orange-deep: #e2641a;
    --yellow: #f6c42a;
    --tab: #e8651e;
    --red-cloth: #d9514c;
    --red-cloth-dark: #b83a38;
    --blue-cloth: #2f86cf;
    --blue-cloth-dark: #1f68ad;
    --wood-light: #b88a5e;
    --wood-dark: #8a6040;
    --ink-brown: #4e3220;
    --navy: #15222d;
    --green: #5cb038;
    --green-dark: #3f9128;
    --frame: #b06a2c;
    --white: #ffffff;
    --ink: #1b1b1b;
  }
  * { margin: 0; padding: 0; box-sizing: border-box; }
  html, body { width: 1200px; height: 688px; overflow: hidden; background: var(--stage); }
  .canvas { position: relative; width: 1200px; height: 688px; }
  .pouch-front {
    position: absolute; left: 359px; top: 24px; width: 482px; height: 640px; overflow: hidden;
    box-shadow: 0 6px 18px rgba(80, 50, 20, .18);
  }
  .pouch-art { position: absolute; inset: 0; }
  .logo-tab {
    position: absolute; left: 207px; top: 0; width: 70px; height: 85px;
    background: var(--tab); border-radius: 0 0 8px 8px;
    display: flex; align-items: flex-end; justify-content: center; padding-bottom: 14px;
    font-family: "Archivo Black", sans-serif; color: var(--white);
    font-size: 15px; line-height: 14px; text-align: center;
  }
  .title-plank {
    position: absolute; left: 79px; top: 118px; width: 321px; height: 133px;
    display: flex; flex-direction: column; align-items: center; justify-content: center;
    color: var(--ink-brown); font-family: "Archivo Black", sans-serif; text-align: center;
  }
  .title-plank .title { font-size: 41px; line-height: 40px; letter-spacing: 1px; text-shadow: 0 1px 0 rgba(255,230,200,.45), 0 -1px 1px rgba(0,0,0,.35); }
  .title-plank .subtitle { margin-top: 6px; font-family: "Poppins", sans-serif; font-weight: 800; font-size: 11.5px; letter-spacing: .2px; }
  .organic-badge {
    position: absolute; left: 0; top: 333px; width: 130px; height: 92px;
    background: var(--navy); border-radius: 0 46px 46px 0;
    display: flex; flex-direction: column; justify-content: center; padding-left: 34px;
    color: var(--white);
  }
  .organic-badge .percent { font-family: "Poppins", sans-serif; font-weight: 800; font-size: 23px; line-height: 24px; }
  .organic-badge .word { font-family: "Pacifico", cursive; font-size: 20px; line-height: 26px; margin-left: -6px; }
  .net-weight { position: absolute; left: 31px; top: 432px; width: 80px; text-align: center; color: var(--ink); font-family: "Poppins", sans-serif; }
  .net-weight .amount { font-family: "Archivo Black", sans-serif; font-size: 19px; line-height: 20px; }
  .net-weight .label { font-weight: 800; font-size: 8px; }
  .claims { position: absolute; left: 335px; top: 570px; display: flex; gap: 6px; }
  .claim { width: 38px; display: flex; flex-direction: column; align-items: center; }
  .claim svg { width: 36px; height: 36px; }
  .claim .label { margin-top: 3px; font-family: "Poppins", sans-serif; font-weight: 700; font-size: 6.5px; line-height: 7px; color: var(--white); text-align: center; }
</style>
</head>
<body>
<main class="canvas">
  <section class="pouch-front">
    <svg class="pouch-art" viewBox="0 0 482 640" width="482" height="640">
      <defs>
        <linearGradient id="wood" x1="0" y1="0" x2="1" y2="1">
          <stop offset="0" stop-color="var(--wood-light)"/>
          <stop offset="1" stop-color="var(--wood-dark)"/>
        </linearGradient>
        <linearGradient id="photo" x1="0" y1="0" x2="0" y2="1">
          <stop offset="0" stop-color="#b9a896"/>
          <stop offset=".45" stop-color="#9a5f35"/>
          <stop offset="1" stop-color="#5b3b26"/>
        </linearGradient>
        <linearGradient id="redCloth" x1="0" y1="0" x2="1" y2="1">
          <stop offset="0" stop-color="var(--red-cloth)"/>
          <stop offset="1" stop-color="var(--red-cloth-dark)"/>
        </linearGradient>
        <linearGradient id="blueCloth" x1="0" y1="0" x2="1" y2="1">
          <stop offset="0" stop-color="var(--blue-cloth)"/>
          <stop offset="1" stop-color="var(--blue-cloth-dark)"/>
        </linearGradient>
        <linearGradient id="greenBand" x1="0" y1="0" x2="0" y2="1">
          <stop offset="0" stop-color="var(--green)"/>
          <stop offset="1" stop-color="var(--green-dark)"/>
        </linearGradient>
        <linearGradient id="stripes" x1="0" y1="0" x2="1" y2="0">
          <stop offset="0" stop-color="var(--orange)"/>
          <stop offset=".5" stop-color="#f0902a"/>
          <stop offset="1" stop-color="var(--orange-deep)"/>
        </linearGradient>
      </defs>

      <rect class="backdrop-pattern" width="482" height="640" fill="url(#stripes)" role="img" aria-label="Orange background with yellow wavy vertical stripes"/>

      <path class="cloth-blue-top" d="M180,0 H482 V380 C470,300 460,220 430,170 C400,130 350,130 300,95 C260,70 210,40 180,0 Z" fill="url(#blueCloth)" role="img" aria-label="Blue patterned Sri Lankan fabric draped across the top corner"/>
      <path class="cloth-red" d="M0,70 C40,60 90,55 120,62 L135,75 C110,90 95,130 90,170 C85,205 70,225 40,232 L0,240 Z" fill="url(#redCloth)" role="img" aria-label="Red patterned fabric fold on the left edge"/>
      <path class="cloth-blue-side" d="M320,248 C345,232 380,238 410,255 C440,270 470,300 482,320 V380 C455,360 420,350 385,335 C355,322 338,300 322,290 Z" fill="url(#blueCloth)" role="img" aria-label="Blue patterned fabric fold on the right edge"/>

      <path class="title-plank-board" d="M82,124 L398,118 L400,246 L84,251 Z" fill="url(#wood)" role="img" aria-label="Cinnamon bark plank behind the product name"/>

      <path class="window-frame" d="M133,552 V362 Q133,314 188,304 Q232,298 243,284 Q254,298 298,304 Q354,314 354,362 V552 Z" fill="var(--frame)"/>
      <path class="window-photo" d="M141,552 V365 Q141,321 191,312 Q232,306 243,294 Q254,306 295,312 Q346,321 346,365 V552 Z" fill="url(#photo)" role="img" aria-label="Photo of rolled cinnamon sticks and ground cinnamon in a wooden scoop"/>

      <path class="band-green" d="M0,548 C40,522 80,518 120,532 C160,546 200,546 243,528 C285,510 325,512 365,530 C405,548 445,548 482,534 V640 H0 Z" fill="url(#greenBand)" role="img" aria-label="Green band with traditional circular pattern"/>
    </svg>

    <div class="logo-tab">LOGO<br>HERE</div>

    <div class="title-plank">
      <div class="title">CEYLON</div>
      <div class="title">CINNAMON</div>
      <div class="subtitle">TRUE CEYLON CINNAMON WITH MCT OIL</div>
    </div>

    <div class="organic-badge">
      <span class="percent">100%</span>
      <span class="word">Organic</span>
    </div>

    <div class="net-weight">
      <div class="amount">250G</div>
      <div class="label">NET WEIGHT</div>
    </div>

    <div class="claims">
      <div class="claim">
        <svg viewBox="0 0 36 36"><circle cx="18" cy="18" r="16" fill="none" stroke="#fff" stroke-width="3"/><line x1="7" y1="29" x2="29" y2="7" stroke="#fff" stroke-width="3"/></svg>
        <span class="label">GLUTEN<br>FREE</span>
      </div>
      <div class="claim">
        <svg viewBox="0 0 36 36"><circle cx="18" cy="18" r="16" fill="#fff"/><path d="M10,18 L16,24 L27,11" fill="none" stroke="var(--green-dark)" stroke-width="4" stroke-linecap="round" stroke-linejoin="round"/></svg>
      </div>
      <div class="claim">
        <svg viewBox="0 0 36 36"><circle cx="18" cy="18" r="16" fill="none" stroke="#fff" stroke-width="3"/><line x1="7" y1="29" x2="29" y2="7" stroke="#fff" stroke-width="3"/></svg>
        <span class="label">GMO<br>FREE</span>
      </div>
    </div>
  </section>
</main>
</body>
</html>
```